Fashion Product Catalogue

We need a catalogue design for a Fashion brand called Fomi.

It will need to be High End, elegant and creative.

The catalogue size should be 21cmx21cm, or A5 Horizontal.

The products can be found on fomi-label.com.au

Contents in details:
1. PAge 1
Cover Page

2. Page 2/3
About us and our products (http://www.fomi-label.com.au/pages/organic-collection)

3. Page 4 and 5
Polo Collection 1 ( http://www.fomi-label.com.au/collections/polo-shirts/Kesta%7CEdged)
Please display 1 main Polo Shirt with different views (front, back, zoom) and available sizes (S, M, L, XL, XXL)
Then show the remaining polo shirts colours in front view only.
Under each product please include: Pantone Colour, SKU/Code Number (QRT114-Blue, QRT114-Black, etc)

4. Page 6 and 7
Polo Collection 2 (http://www.fomi-label.com.au/collections/polo-shirts/Meridian%7CPlain-Polo)
Under each product please include: Pantone Colour, SKU/Code Number (QRT115-Blue, QRT115-Black, etc)

5. Page 7
V Neck Collection
http://www.fomi-label.com.au/collections/mens-plain-t-shirts/bastien-basic-v-neck
Please display 1 main T Shirt with different views (front, back, zoom) and available sizes (S, M, L, XL)
Then show the remaining T-Shirts colours in front view only.
Under each product please include: Pantone Colour Block, Pantone Colour Code, SKU/Code Number (QRT116-Blue, QRT116-Black, etc)

6. Page 8
Raw V Neck Collection
http://www.fomi-label.com.au/collections/mens-fashion-tees/hollis-raw-v-neck

Same as above

7. Page 9
http://www.fomi-label.com.au/collections/mens-plain-t-shirts/prael-plain-tee

Same as above

8. More to follow later after I approve of the first pages designs

You may submit a few pages for view at first. I will then approve or reject and then choose a few designers who will get the job and be appointed for other catalogue designs as well.

You may request other pictures if necessary and we also have Raw files that will be provided to designers once their skill and creativity is assessed.

Target Market(s)

Male 24 years +

Industry/Entity Type

Fashion

Requirements
Must have
• A feel for Organic Clothing. Leaves, wood design, etc
• Example for cover: https://www.social-example.net/fomilabelau/photos/a.2648193057724318.2084913375.2641177094862235/2648193310527471/?type=1&theater
• See attachment for brand logo and psd of inspiration for the cover.

```html
<!DOCTYPE html>
<html lang="en">
<head>
<meta charset="utf-8">
<title>Fomi — About Us Spread</title>
<link href="https://fonts.googleapis.com/css2?family=Crimson+Text:wght@400&display=swap" rel="stylesheet">
<style>
  :root {
    --backdrop: #cdd6df;
    --paper: #f4f4f2;
    --ink: #2e2e2c;
    --mist-light: #eceadb;
    --mist-mid: #d3d2b6;
    --mist-deep: #aeb08c;
    --tree-dark: #38422a;
    --grass: #5f8230;
    --grass-light: #7fa040;
    --gutter-shade: rgba(0, 0, 0, 0.18);
  }
  * { margin: 0; padding: 0; box-sizing: border-box; }
  html, body {
    width: 1200px;
    height: 800px;
    overflow: hidden;
    background: var(--backdrop);
  }
  .spread {
    position: absolute;
    left: 80px;
    top: 140px;
    width: 1040px;
    height: 520px;
    box-shadow: 0 10px 30px rgba(40, 50, 60, 0.18);
    overflow: hidden;
  }
  .landscape {
    position: absolute;
    inset: 0;
    background:
      linear-gradient(180deg,
        var(--mist-light) 0%,
        var(--mist-light) 18%,
        var(--mist-mid) 34%,
        var(--mist-light) 40%,
        var(--mist-deep) 52%,
        var(--tree-dark) 66%,
        var(--tree-dark) 72%,
        var(--grass) 80%,
        var(--grass-light) 100%);
  }
  .gutter {
    position: absolute;
    left: 500px;
    top: 0;
    width: 40px;
    height: 100%;
    background: linear-gradient(90deg, transparent, var(--gutter-shade) 50%, transparent);
  }
  .about-panel {
    position: absolute;
    left: 0;
    top: 80px;
    bottom: 0;
    width: 305px;
    background: var(--paper);
    padding: 28px 26px 24px 28px;
  }
  .about-copy {
    font-family: "Crimson Text", serif;
    font-size: 11px;
    line-height: 1.45;
    color: var(--ink);
    text-align: justify;
    hyphens: auto;
  }
  .about-copy p + p { margin-top: 11px; }
</style>
</head>
<body>
  <section class="spread">
    <div class="landscape" role="img" aria-label="Misty rolling countryside at dawn with layered hills, a line of trees and a green meadow across both pages"></div>
    <div class="gutter"></div>
    <article class="about-panel">
      <div class="about-copy">
        <p>Formed up in Australia, Fomi answers the call of nature. We believe that through clothing and fashion should never come at the detriment of any human being or the environment.</p>
        <p>We strive to bring you the highest quality garments made from the world’s best natural fibres, we carefully select our manufacturers to ensure quality and a highest level of social and ecological responsibility along the entire supply chain. Moreover, wherever possible, we reduce the amount of plastic used in designing our Collections and also convey our products to you in the most sustainable manner.</p>
        <p>Fomi’s commitment is not only towards the earth but also the best feel against your skin with the highest quality fibres. In our journey to find the perfect balance between sustainability and style, we promise to always make you feel great and look your best.</p>
      </div>
    </article>
  </section>
</body>
</html>
```